Personal Business Card design contest for freelance work

Include

Proflink.example/in/DanielMWhitacre (as URL and/or QR Code)
Daniel Whitacre
(555) 014-2938
DanielMWhitacre@Mailnest.example
Houston, TX

Industry/Entity Type

Business

```html
<!DOCTYPE html>
<html lang="en">
<head>
<meta charset="utf-8">
<title>Daniel Whitacre — Business Card</title>
<link rel="stylesheet" href="https://fonts.googleapis.com/css2?family=Open+Sans:wght@400;600&display=swap">
<style>
  :root {
    --backdrop: #2a2522;
    --card-front: #1b1c1e;
    --card-front-edge: #141516;
    --card-back: #111213;
    --accent: #e9a46c;
    --text-light: #ecebe8;
    --divider: #4a4b4d;
    --figure-skin: #d9a27c;
    --figure-suit: #232427;
    --figure-emboss: #1d1e20;
  }
  * { margin: 0; padding: 0; box-sizing: border-box; }
  html, body { width: 1200px; height: 844px; overflow: hidden; }
  body {
    background: var(--backdrop);
    font-family: "Open Sans", Arial, sans-serif;
    position: relative;
  }
  .card {
    position: absolute;
    top: 262px;
    width: 560px;
    height: 320px;
    border-radius: 3px;
    box-shadow: 0 12px 30px rgba(0,0,0,0.45);
  }
  .card--front {
    left: 30px;
    background: linear-gradient(150deg, #232427 0%, var(--card-front) 45%, var(--card-front-edge) 100%);
  }
  .card--back {
    left: 610px;
    background: var(--card-back);
  }
  .portrait {
    position: absolute;
    left: 70px;
    top: 62px;
    width: 150px;
    height: 222px;
  }
  .divider {
    position: absolute;
    left: 250px;
    top: 58px;
    width: 1px;
    height: 200px;
    background: var(--divider);
  }
  .details {
    position: absolute;
    left: 272px;
    top: 62px;
    color: var(--text-light);
  }
  .details__name {
    font-size: 25px;
    font-weight: 400;
    color: var(--accent);
    margin-bottom: 14px;
    letter-spacing: 0.2px;
  }
  .details__contact {
    list-style: none;
    font-size: 13px;
    line-height: 18px;
    margin-bottom: 14px;
  }
  .details__label { color: var(--accent); margin-right: 4px; }
  .details__address { font-size: 13px; line-height: 18px; }
  .emboss-figure {
    position: absolute;
    left: 235px;
    top: 40px;
    width: 100px;
    height: 170px;
  }
</style>
</head>
<body>
  <section class="card card--front">
    <svg class="portrait" viewBox="0 0 150 222" role="img" aria-label="Cartoon caricature of Daniel Whitacre in a dark suit holding papers">
      <defs>
        <linearGradient id="portrait-tone" x1="0" y1="0" x2="0" y2="1">
          <stop offset="0" stop-color="var(--figure-skin)" stop-opacity="0.55"/>
          <stop offset="0.35" stop-color="var(--figure-suit)"/>
          <stop offset="1" stop-color="var(--figure-suit)"/>
        </linearGradient>
      </defs>
      <rect x="0" y="0" width="150" height="210" rx="8" fill="url(#portrait-tone)"/>
      <ellipse cx="80" cy="212" rx="48" ry="8" fill="#8fa9b3"/>
    </svg>
    <div class="divider"></div>
    <div class="details">
      <h1 class="details__name">Daniel Whitacre</h1>
      <ul class="details__contact">
        <li><span class="details__label">T:</span>(555) 014-2938</li>
        <li><span class="details__label">E:</span>DanielMWhitacre@Mailnest.example</li>
        <li><span class="details__label">W:</span>Proflink.example/in/DanielMWhitacre</li>
      </ul>
      <p class="details__address">Houston, TX<br>United States</p>
    </div>
  </section>

  <section class="card card--back">
    <svg class="emboss-figure" viewBox="0 0 100 170" role="img" aria-label="Faint embossed caricature figure of Daniel Whitacre">
      <defs>
        <linearGradient id="emboss-tone" x1="0" y1="0" x2="1" y2="1">
          <stop offset="0" stop-color="#26272a"/>
          <stop offset="1" stop-color="var(--figure-emboss)"/>
        </linearGradient>
      </defs>
      <rect x="0" y="0" width="100" height="162" rx="8" fill="url(#emboss-tone)"/>
      <ellipse cx="60" cy="164" rx="34" ry="5" fill="#202123"/>
    </svg>
  </section>
</body>
</html>
```